Lanternfield Drinks business cards

We need a business card design for our new logo. The company is modern, progressive, professional, yet approachable. The key products are ready to drink bottles and cans of coffee based beverages.
These cards will be a critical part of the first impression made by our sales organization, business development team, and all external facing personnel.
Card can be a vertical or horizontal orientation.

Target Market(s)

Customers, suppliers, business partners

Industry/Entity Type

Business

Contact Information for Business Card

Business cards should feature Company Name and Logo.

Font styles to use
Serif

Colors

Designer to choose colors to be used in the design.

Requirements
Must have
• Strong readability of Name, phone #, mobile number and email address.
• Job title, website url, Street Address, and other details can be secondary level readability.
Nice to have
• High impact, simplistic quality design.
• Ok to utilize the 'H in the box' separate from the company name

```html
<!DOCTYPE html>
<html lang="en">
<head>
<meta charset="utf-8">
<title>Lanternfield Drinks – Business Cards</title>
<link rel="stylesheet" href="https://fonts.googleapis.com/css2?family=Cinzel:wght@600&family=Marcellus&display=swap">
<style>
  :root {
    --backdrop: #d9d9d9;
    --orange: #e8391a;
    --orange-soft: #ef4a22;
    --ink: #1b1b1b;
    --card-black: #222222;
    --white: #f2f2f2;
  }
  html, body {
    margin: 0;
    width: 1200px;
    height: 1021px;
    overflow: hidden;
    background: var(--backdrop);
  }
  .canvas {
    position: relative;
    width: 1200px;
    height: 1021px;
  }
  .card {
    position: absolute;
    width: 640px;
    height: 366px;
    box-shadow: 0 14px 30px rgba(0,0,0,.25);
  }
  .card-front {
    left: 80px;
    top: 90px;
    background: var(--orange);
    display: flex;
    align-items: center;
    justify-content: center;
  }
  .card-back {
    left: 480px;
    top: 565px;
    background: var(--card-black);
    color: var(--white);
    font-family: "Marcellus", serif;
  }
  .brand {
    display: flex;
    align-items: center;
    gap: 18px;
    font-family: "Cinzel", serif;
    font-weight: 600;
  }
  .brand-square {
    width: 64px;
    height: 64px;
    border: 5px solid var(--ink);
    box-sizing: border-box;
  }
  .brand-name {
    font-size: 34px;
    letter-spacing: 1px;
    color: var(--ink);
  }
  .card-back .brand {
    position: absolute;
    top: 38px;
    right: 40px;
    flex-direction: column;
    gap: 12px;
    align-items: center;
  }
  .card-back .brand-square {
    width: 46px;
    height: 46px;
    border: 4px solid var(--orange);
  }
  .card-back .brand-name {
    font-size: 24px;
    color: var(--orange);
  }
  .holder {
    position: absolute;
    left: 56px;
    top: 150px;
  }
  .holder-name {
    font-size: 24px;
    letter-spacing: 1px;
    margin: 0;
  }
  .holder-title {
    font-size: 16px;
    letter-spacing: 1px;
    color: var(--orange);
    margin: 4px 0 0;
  }
  .rule {
    width: 62px;
    height: 3px;
    background: var(--orange);
    margin: 26px 0 22px 22px;
  }
  .contacts {
    list-style: none;
    margin: 0 0 0 22px;
    padding: 0;
    font-size: 15px;
  }
  .contacts li {
    display: flex;
    align-items: center;
    gap: 12px;
    margin-bottom: 8px;
  }
  .contacts svg { width: 13px; height: 13px; fill: var(--orange); }
  .website {
    position: absolute;
    right: 40px;
    bottom: 96px;
    font-size: 14px;
    color: var(--orange);
    letter-spacing: .5px;
  }
</style>
</head>
<body>
<main class="canvas">
  <section class="card card-front" aria-label="Card front">
    <div class="brand">
      <span class="brand-square"></span>
      <span class="brand-name">LANTERNFIELD DRINKS</span>
    </div>
  </section>

  <section class="card card-back" aria-label="Card back">
    <div class="brand">
      <span class="brand-square"></span>
      <span class="brand-name">LANTERNFIELD DRINKS</span>
    </div>

    <div class="holder">
      <p class="holder-name">YOUR NAME</p>
      <p class="holder-title">JOB TITLE</p>
      <div class="rule"></div>
      <ul class="contacts">
        <li>
          <svg viewBox="0 0 16 16" aria-hidden="true"><path d="M3 1h3l1.5 4-2 1.3a9 9 0 0 0 4.2 4.2L11 8.5l4 1.5v3a2 2 0 0 1-2 2A13 13 0 0 1 1 3a2 2 0 0 1 2-2z"/></svg>
          <span>+971 XXXXXXX</span>
        </li>
        <li>
          <svg viewBox="0 0 16 16" aria-hidden="true"><path d="M4 0h8a1 1 0 0 1 1 1v14a1 1 0 0 1-1 1H4a1 1 0 0 1-1-1V1a1 1 0 0 1 1-1zm1 2v10h6V2zm3 11a1 1 0 1 0 0 2 1 1 0 0 0 0-2z"/></svg>
          <span>+971 YYYYYY</span>
        </li>
        <li>
          <svg viewBox="0 0 16 16" aria-hidden="true"><path d="M0 3h16v10H0zm1.5 1.2L8 9l6.5-4.8V4h-13z"/></svg>
          <span>x@y.com</span>
        </li>
      </ul>
      <div class="rule"></div>
    </div>

    <p class="website">www.yourwebsite.com</p>
  </section>
</main>
</body>
</html>
```